Local Flower Farm Needs Business Card Design

I need business cards designed for a flower farm based in Eudora, Kansas.
Business Info:
We are a local cut flower farm located in Eudora, Kansas, founded by Darla Hoffstrom. What started as a passion for agriculture and search for more joy in daily life has blossomed into a small business dedicated to providing the community with beautiful, fresh, and sustainable flowers. We specialize in local, seasonal blooms, ensuring that every petal reflects the care and dedication we pour into our craft. Our mission is to deliver the highest quality flowers directly to our customers through local farmers markets and to florists who share our commitment to sustainability. Join us in celebrating the beauty of nature, one bloom at a time!
Contact Details:
Darla Hoffstrom
Owner
Phone 913-555-0147
Facebook: Lorabelle Quinn Blossoms
Instagram: @LorabelleQuinnBlossoms
Website: LorabelleQuinnBlossoms.example
Target Market(s)
Wholesale to Florists and Direct to Consumer via Farmers Market
Industry/Entity Type
Florist, Farm
Contact Information for Business Card
Name, Contact Info, Logo
Look and feel

```html
<!DOCTYPE html>
<html lang="en">
<head>
<meta charset="utf-8">
<title>Lorabelle Quinn Blossoms – Business Cards</title>
<link rel="stylesheet" href="https://fonts.googleapis.com/css2?family=Crimson+Pro:wght@400;700&display=swap">
<style>
  :root {
    --backdrop: #e7e8eb;
    --card: #ffffff;
    --ink: #16302f;
    --ink-soft: #4a5554;
    --rule: #9aa3a2;
    --petal: #f4f6f5;
  }
  * { box-sizing: border-box; margin: 0; padding: 0; }
  html, body { width: 1200px; height: 800px; overflow: hidden; }
  body {
    background: var(--backdrop);
    font-family: "Crimson Pro", Georgia, serif;
    color: var(--ink);
    position: relative;
  }
  .card {
    position: absolute;
    width: 525px;
    height: 300px;
    background: var(--card);
    overflow: hidden;
    box-shadow: 0 6px 18px rgba(0,0,0,0.12);
  }
  .card--front { left: 50px; top: 250px; }
  .card--back { left: 625px; top: 250px; }
  .card__band { position: absolute; inset: 0; width: 100%; height: 100%; }
  .card__band path { fill: var(--ink); }

  .floral {
    position: absolute;
    border-radius: 40% 55% 45% 50%;
  }
  .card--front .floral {
    left: 40px; top: 20px; width: 270px; height: 130px;
    background: linear-gradient(135deg, var(--ink) 0%, #5d7270 45%, var(--petal) 100%);
    opacity: 0.5;
  }
  .card--back .floral {
    left: 412px; top: 45px; width: 100px; height: 240px;
    background: linear-gradient(200deg, var(--petal) 0%, #6a7e7c 50%, var(--ink) 100%);
    opacity: 0.5;
  }

  .brand-seal {
    position: absolute;
    width: 118px; height: 118px;
    border: 1.5px solid var(--ink);
    border-radius: 50%;
    display: flex; align-items: center; justify-content: center;
    text-align: center;
    font-size: 15px;
    line-height: 1.15;
    font-weight: 400;
    color: var(--ink);
    letter-spacing: 0.06em;
    text-transform: uppercase;
    padding: 12px;
  }
  .card--front .brand-seal { left: 290px; top: 160px; }
  .card--back .brand-seal { left: 85px; top: 18px; width: 100px; height: 100px; font-size: 13px; }

  .contact { position: absolute; left: 40px; top: 128px; width: 320px; }
  .contact__name { font-size: 19px; font-weight: 700; line-height: 1.1; }
  .contact__role { font-size: 14px; color: var(--ink-soft); margin-bottom: 8px; }
  .contact__line {
    display: flex; align-items: center; gap: 6px;
    font-size: 14px; color: var(--ink-soft); line-height: 1.45;
    white-space: nowrap;
  }
  .contact__line--social { font-size: 12px; gap: 5px; }
  .contact__icon { width: 13px; height: 13px; flex: none; }
  .contact__icon circle, .contact__icon path { fill: none; stroke: var(--ink); stroke-width: 1.4; }
  .contact__dot {
    width: 10px; height: 10px; border-radius: 50%;
    background: var(--ink); flex: none;
  }
  .contact__rule { border: 0; border-top: 1px solid var(--rule); margin: 5px 0; width: 320px; }
  .contact__sep { color: var(--rule); margin: 0 2px; }
</style>
</head>
<body>

  <section class="card card--front" aria-label="Business card front">
    <svg class="card__band" viewBox="0 0 525 300" preserveAspectRatio="none" aria-hidden="true">
      <path d="M0,0 H440 C390,40 330,70 290,90 C220,120 120,160 0,195 Z"/>
    </svg>
    <div class="floral" role="img" aria-label="White line-drawn flower stems with tulips and buds"></div>
    <div class="brand-seal">Lorabelle Quinn Blossoms</div>
  </section>

  <section class="card card--back" aria-label="Business card back">
    <svg class="card__band" viewBox="0 0 525 300" preserveAspectRatio="none" aria-hidden="true">
      <path d="M345,0 H525 V300 H400 C420,230 380,170 370,110 C362,60 350,30 345,0 Z"/>
    </svg>
    <div class="floral" role="img" aria-label="Upright line-drawn bouquet of tulips and leaves"></div>
    <div class="brand-seal">Lorabelle Quinn Blossoms</div>

    <div class="contact">
      <p class="contact__name">Darla Hoffstrom</p>
      <p class="contact__role">Owner</p>
      <p class="contact__line">
        <svg class="contact__icon" viewBox="0 0 14 14" aria-hidden="true">
          <path d="M3,1.5 L5,1.5 L6,4.5 L4.5,5.5 C5.3,7.3 6.7,8.7 8.5,9.5 L9.5,8 L12.5,9 L12.5,11 C12.5,12 11.5,12.5 10.5,12.5 C5.5,12 2,8.5 1.5,3.5 C1.5,2.5 2,1.5 3,1.5 Z"/>
        </svg>
        913-555-0147
      </p>
      <p class="contact__line">
        <svg class="contact__icon" viewBox="0 0 14 14" aria-hidden="true">
          <circle cx="7" cy="7" r="5.5"/>
          <path d="M1.5,7 H12.5 M7,1.5 C4.5,4 4.5,10 7,12.5 M7,1.5 C9.5,4 9.5,10 7,12.5"/>
        </svg>
        LorabelleQuinnBlossoms.example
      </p>
      <hr class="contact__rule">
      <p class="contact__line contact__line--social">
        <span class="contact__dot" aria-hidden="true"></span>
        <span>Lorabelle Quinn Blossoms</span>
        <span class="contact__sep">|</span>
        <span class="contact__dot" aria-hidden="true"></span>
        <span>@LorabelleQuinnBlossoms</span>
      </p>
      <hr class="contact__rule">
    </div>
  </section>

</body>
</html>
```